Optometrist/Eye Care Clinic Business card with new logo attached

We are a small, independent eye care clinic in Canada. We have recently updated our logo (as attached), and would like a professional, modern and health care oriented business card to highlight our office details and our optometrist. We'd like to incorporate the blue colours as seen on our logo.

Target Market(s)

demographic: age 35-65 male/female equal

Industry/Entity Type

Health Care

Contact Information for Business Card

Name of clinic: "Marrow Bend Eye Care Optometry"

Font styles to use
Sans Serif

Colors
0355a3

Requirements
Must have
• our website: marrowbendeyecare.com
• Dr Lena Quorvik
• Optometrist
• 217-392 E Halvering Ave
• Vancouver BC V6R 3J8
• P: 604-319-2058
• E: info@marrowbendeyecare.com
Nice to have
• front side: logo/name of clinic as seen on logo attached and website
• backside: logo on the left side, and name/title/address/phone/email

```html
<!DOCTYPE html>
<html lang="en">
<head>
<meta charset="utf-8">
<title>Marrow Bend Eye Care Optometry – Business Card</title>
<link rel="stylesheet" href="https://fonts.googleapis.com/css2?family=Mulish:wght@400;600&display=swap">
<style>
  :root {
    --brand-blue: #0355a3;
    --brand-blue-light: #2a6db0;
    --band-blue: #0a4fa0;
    --paper: #f7f8fa;
    --ink: #1f3550;
    --stage-top: #eef0f4;
    --stage-bottom: #d9dde4;
    --white: #ffffff;
  }
  * { margin: 0; padding: 0; box-sizing: border-box; }
  html, body { width: 1200px; height: 675px; overflow: hidden; }
  body {
    font-family: "Mulish", sans-serif;
    background: linear-gradient(180deg, var(--stage-top), var(--stage-bottom));
    position: relative;
  }
  .card {
    position: absolute;
    top: 194px;
    width: 500px;
    height: 286px;
    border-radius: 4px;
    box-shadow: 0 14px 30px rgba(30, 45, 70, 0.22);
    overflow: hidden;
  }

  /* Back side */
  .card-back {
    left: 60px;
    background: linear-gradient(135deg, var(--brand-blue-light), var(--brand-blue));
    color: var(--white);
  }
  .back-identity {
    position: absolute;
    left: 40px;
    top: 120px;
    width: 176px;
    text-align: right;
  }
  .doctor-name {
    font-size: 21px;
    font-weight: 600;
    letter-spacing: 0.3px;
    white-space: nowrap;
  }
  .doctor-title {
    font-size: 11px;
    letter-spacing: 4.6px;
    margin-top: 2px;
    margin-right: -4px;
  }
  .back-divider {
    position: absolute;
    left: 232px;
    top: 104px;
    width: 1px;
    height: 76px;
    background: rgba(255, 255, 255, 0.75);
  }
  .contact-list {
    position: absolute;
    left: 252px;
    top: 108px;
    list-style: none;
    font-size: 12.5px;
    line-height: 17px;
    white-space: nowrap;
  }
  .contact-list li { display: flex; align-items: center; gap: 9px; }
  .contact-list .icon { width: 11px; height: 11px; flex: none; }
  .contact-list .no-icon { padding-left: 20px; }

  /* Front side */
  .card-front {
    left: 640px;
    background: var(--paper);
  }
  .clinic-name {
    position: absolute;
    left: 0; right: 0;
    top: 96px;
    margin: 0 auto;
    width: 340px;
    font-size: 20px;
    font-weight: 400;
    letter-spacing: 2.4px;
    text-transform: uppercase;
    color: var(--ink);
    text-align: center;
    line-height: 1.4;
  }
  .web-band {
    position: absolute;
    left: 0; right: 0; bottom: 0;
    height: 46px;
    background: var(--band-blue);
    color: var(--white);
    font-size: 15px;
    letter-spacing: 0.4px;
    display: flex;
    align-items: center;
    justify-content: center;
  }
</style>
</head>
<body>

<section class="card card-back" aria-label="Business card, back">
  <div class="back-identity">
    <p class="doctor-name">Dr Lena Quorvik</p>
    <p class="doctor-title">OPTOMETRIST</p>
  </div>
  <div class="back-divider"></div>
  <ul class="contact-list">
    <li>
      <svg class="icon" viewBox="0 0 24 24" aria-hidden="true"><path fill="#fff" d="M6.6 10.8a15.1 15.1 0 0 0 6.6 6.6l2.2-2.2a1 1 0 0 1 1-.25 11.4 11.4 0 0 0 3.6.57 1 1 0 0 1 1 1V20a1 1 0 0 1-1 1A17 17 0 0 1 3 4a1 1 0 0 1 1-1h3.5a1 1 0 0 1 1 1c0 1.250.2 2.450.57 3.570a1 1 0 0 1-.25 1z"/></svg>
      604-319-2058
    </li>
    <li>
      <svg class="icon" viewBox="0 0 24 24" aria-hidden="true"><rect x="2" y="5" width="20" height="14" rx="1.5" fill="none" stroke="#fff" stroke-width="2"/><path d="M3 6l9 7 9-7" fill="none" stroke="#fff" stroke-width="2"/></svg>
      info@marrowbendeyecare.com
    </li>
    <li>
      <svg class="icon" viewBox="0 0 24 24" aria-hidden="true"><path fill="#fff" d="M12 2a7 7 0 0 0-7 7c0 5.2 7 13 7 13s7-7.8 7-13a7 7 0 0 0-7-7zm0 9.5A2.5 2.5 0 1 1 12 6.5a2.5 2.5 0 0 1 0 5z"/></svg>
      217-392 E Halvering Ave
    </li>
    <li class="no-icon">Vancouver BC V6R 3J8</li>
  </ul>
</section>

<section class="card card-front" aria-label="Business card, front">
  <p class="clinic-name">Marrow Bend Eye Care Optometry</p>
  <div class="web-band">marrowbendeyecare.com</div>
</section>

</body>
</html>
```